Lumbrix - "Where Pest Control is Free for Life..." Please see pitch deck...

Project goal, that this is a reusable template, not a one-off card
Brand and design direction, follow the logo, use the brand palette (with a color swatch table), typography and layout guidance
The John Doe placeholder content as a clean field-by-field table (name, title, company, address, office, cell, fax, email, lumbrix.example)
Print specs, 3.5 × 2 in trim, 0.125 in bleed, 300 DPI, CMYK, crop marks
Deliverables, layered editable PSD (your primary ask) plus vector .AI/.EPS and a press-ready PDF/X-1a, with fonts packaged
What you'll provide (logo, colors, fonts)
Process and sign-off, concept first, then full file package on approval.
Populate every field with this John Doe placeholder data so we can see the layout fully built out. We will replace it per person.
Name John Doe
Title Title / Position
Company Lumbrix
Address 48 Harbor Road, Suite 210, Brookfield, ST 10482
Office (555) 014-2200
Cell (555) 014-2231
Fax (555) 014-2299
Email johndoe@lumbrix.example
Website lumbrix.example

We need the working, editable source files so we can update them ourselves, plus a ready-to-print export:
1. Photoshop (.PSD) — fully layered and editable, with each contact field on its own labeled text layer. This is the primary requested format.
2. Vector source — the press-standard editable format, Adobe Illustrator (.AI) and/or .EPS, since vector is preferred for crisp text and logos at print.
3. Print-ready PDF — press-quality (PDF/X-1a), CMYK, with bleed and crop marks, both sides.
4. Packaged fonts and links — include or list all fonts used, and package any linked assets so the files open correctly on our end.

Why both PSD and vector
The PSD covers our request directly and is easy for us to edit. Vector (.AI/.EPS) is what most commercial printers actually prefer for type and logos because it stays razor-sharp at any size. Providing both keeps us flexible no matter which printer we use. Have fun and keep it modern and cool the designer of the logo did a great job, see what you can do.

```html
<!DOCTYPE html>
<html lang="en">
<head>
<meta charset="utf-8">
<title>Lumbrix Business Card Template</title>
<link rel="stylesheet" href="https://fonts.googleapis.com/css2?family=Montserrat:ital,wght@0,400;0,500;0,700;0,800;1,400&display=swap">
<style>
  :root {
    --backdrop: #ebe5e0;
    --navy: #161d36;
    --navy-deep: #0d1328;
    --teal: #1eb3c3;
    --white: #f4f4f2;
    --card-w: 614px;
    --card-h: 362px;
  }
  * { box-sizing: border-box; margin: 0; padding: 0; }
  html, body {
    width: 1067px; height: 1200px; overflow: hidden;
    background: var(--backdrop);
    font-family: "Montserrat", sans-serif;
  }
  .canvas { position: relative; width: 1067px; height: 1200px; }
  .card {
    position: absolute; left: 245px;
    width: var(--card-w); height: var(--card-h);
    background: linear-gradient(180deg, var(--navy) 0%, var(--navy-deep) 100%);
    box-shadow: 0 10px 24px rgba(60, 45, 30, 0.25);
    overflow: hidden;
  }
  .card--front { top: 196px; }
  .card--back { top: 661px; }
  .accent-strip {
    position: absolute; top: 0; bottom: 0; width: 40px;
    background: var(--teal);
  }
  .card--front .accent-strip { right: 0; }
  .card--back .accent-strip { left: 0; }

  /* Front */
  .brand-lockup {
    position: absolute; left: 0; right: 40px; top: 136px;
    text-align: center;
  }
  .brand-name {
    font-weight: 800; font-size: 60px; line-height: 1;
    color: var(--white); letter-spacing: -1px;
  }
  .brand-tagline {
    margin-top: 8px; font-weight: 800; font-size: 12.5px;
    color: var(--white); letter-spacing: 0.6px;
  }
  .brand-subline {
    margin-top: 1px; font-style: italic; font-size: 10px;
    color: var(--teal); letter-spacing: 0.3px;
  }

  /* Back */
  .person { position: absolute; left: 101px; top: 34px; }
  .person-name {
    font-weight: 800; font-size: 34px; line-height: 1;
    color: var(--teal);
  }
  .person-title {
    margin-top: 14px; font-weight: 500; font-size: 14.5px;
    color: var(--white); letter-spacing: 1.2px;
  }
  .address {
    position: absolute; right: 42px; top: 38px;
    text-align: right; font-style: normal;
    font-size: 13px; line-height: 17px;
    color: var(--teal); letter-spacing: 1.4px;
  }
  .contact-list {
    position: absolute; left: 100px; top: 186px;
    list-style: none;
  }
  .contact-item {
    display: flex; align-items: center; height: 27px;
    font-size: 12.5px; color: var(--white); letter-spacing: 1.5px;
  }
  .contact-icon {
    width: 19px; height: 19px; margin-right: 16px;
    flex: none;
  }
  .contact-label { display: inline-block; width: 23px; }
  .back-brand {
    position: absolute; right: 42px; bottom: 42px;
    font-weight: 800; font-size: 27px; line-height: 1;
    color: var(--white); letter-spacing: -0.5px;
  }
</style>
</head>
<body>
<main class="canvas">

  <section class="card card--front" aria-label="Business card front">
    <div class="brand-lockup">
      <div class="brand-name">Lumbrix</div>
      <div class="brand-tagline">WE GUARD WHERE YOU LIVE</div>
      <div class="brand-subline">Pest control free for life</div>
    </div>
    <div class="accent-strip" role="img" aria-label="Teal window-grid pattern strip"></div>
  </section>

  <section class="card card--back" aria-label="Business card back">
    <div class="accent-strip" role="img" aria-label="Teal window-grid pattern strip"></div>

    <div class="person">
      <h1 class="person-name">John Doe</h1>
      <p class="person-title">Title/Position</p>
    </div>

    <address class="address">
      48 Harbor Road,<br>
      Suite 210,Brookfield,<br>
      ST 10482
    </address>

    <ul class="contact-list">
      <li class="contact-item">
        <svg class="contact-icon" viewBox="0 0 20 20" aria-hidden="true">
          <rect width="20" height="20" rx="4" fill="var(--teal)"/>
          <rect x="4" y="6" width="12" height="8.5" fill="none" stroke="var(--navy)" stroke-width="1.2"/>
          <path d="M4 6l6 5 6-5M4 14.5l4.5-4M16 14.5l-4.5-4" fill="none" stroke="var(--navy)" stroke-width="1.2"/>
        </svg>
        johndoe@lumbrix.example
      </li>
      <li class="contact-item">
        <svg class="contact-icon" viewBox="0 0 20 20" aria-hidden="true">
          <rect width="20" height="20" rx="4" fill="var(--teal)"/>
          <g fill="none" stroke="var(--navy)" stroke-width="1.1">
            <circle cx="10" cy="10" r="6"/>
            <ellipse cx="10" cy="10" rx="2.6" ry="6"/>
            <path d="M4 10h12M5 7h10M5 13h10"/>
          </g>
        </svg>
        lumbrix.example
      </li>
      <li class="contact-item">
        <svg class="contact-icon" viewBox="0 0 20 20" aria-hidden="true">
          <rect width="20" height="20" rx="4" fill="var(--teal)"/>
          <g fill="none" stroke="var(--navy)" stroke-width="1.1">
            <rect x="6" y="4" width="8" height="12"/>
            <path d="M8 7h1.5M10.5 7H12M8 9.5h1.5M10.5 9.5H12M8 12h1.5M10.5 12H12M9 16v-2h2v2"/>
          </g>
        </svg>
        <span class="contact-label">O:</span>(555) 014-2200
      </li>
      <li class="contact-item">
        <svg class="contact-icon" viewBox="0 0 20 20" aria-hidden="true">
          <rect width="20" height="20" rx="4" fill="var(--teal)"/>
          <path d="M6.5 4.5l2 2.8-1.2 1.4c.8 1.8 2.2 3.2 4 4l1.4-1.2 2.8 2-1 1.8c-4.6-.4-8.2-4-8.6-8.6z" fill="none" stroke="var(--navy)" stroke-width="1.1" stroke-linejoin="round"/>
        </svg>
        <span class="contact-label">P:</span>(555) 014-2231
      </li>
      <li class="contact-item">
        <svg class="contact-icon" viewBox="0 0 20 20" aria-hidden="true">
          <rect width="20" height="20" rx="4" fill="var(--teal)"/>
          <g fill="none" stroke="var(--navy)" stroke-width="1.1">
            <rect x="7" y="4" width="6" height="4"/>
            <rect x="4.5" y="8" width="11" height="6" rx="1"/>
            <rect x="7" y="12" width="6" height="4"/>
          </g>
        </svg>
        <span class="contact-label">F:</span>(555) 014-2299
      </li>
    </ul>

    <div class="back-brand">Lumbrix</div>
  </section>

</main>
</body>
</html>
```